Personalised Poetry business needs a business card designed

I am a writer that specialises in personalised poetry for people for significant life events.
I want a business card that stands out and portrays class and professionalism but is also welcoming & indicates warmth and honesty.
I'm happy with the logo that was designed for me, I would like to see it in raised print on the business card. I am open to suggestions on colours but think perhaps gold or silver writing for the logo would look good. I would like just the logo and my name and contact details on the front of the card. On the back of the card, I would like a list of the different events I provide poems for I will upload a photo of my current business card for reference. My current logo has a shading behind it that I don't like, I just want the words of the logo without any background colour

Target Market(s)

People wanting to provide a unique gift to someone special in their life

Industry/Entity Type

Writer

Contact Information for Business Card

Logo, my name and contact details on the front and a list of all the events I write poetry for on the back

Font styles to use
Script

Requirements
Must have
• I would like to see the logo, if possible, in a raised type of print on the card so that you can feel the actual words. I would like to have a glossy finish to the card and be able to print it on good quality board
Should not have
• The shading that is currently behind the logo on my current business card

```html
<!DOCTYPE html>
<html lang="en">
<head>
<meta charset="utf-8">
<title>Lines for Always – Business Card</title>
<link href="https://fonts.googleapis.com/css2?family=Quicksand:wght@400;500&family=Great+Vibes&display=swap" rel="stylesheet">
<style>
  :root {
    --page: #ffffff;
    --card: #262850;
    --swirl: rgba(37, 53, 102, 0.55);
    --gold: #f4e31c;
    --white: #ffffff;
    --rule: #8a7f55;
    --icon: #8c8fb0;
  }
  * { margin: 0; padding: 0; box-sizing: border-box; }
  html, body { width: 1200px; height: 1200px; overflow: hidden; background: var(--page); }
  body { position: relative; font-family: "Quicksand", sans-serif; }

  .card {
    position: absolute;
    left: 158px;
    width: 891px;
    height: 494px;
    background: var(--card);
    border-radius: 10px;
    overflow: hidden;
  }
  .card--front { top: 94px; }
  .card--back { top: 619px; }

  .flourish {
    position: absolute;
    inset: 0;
  }
  .front .flourish { background: radial-gradient(ellipse 55% 60% at 78% 50%, var(--swirl), transparent 70%); }
  .back .flourish { background: radial-gradient(ellipse 50% 65% at 80% 45%, var(--swirl), transparent 70%); }

  .brand-name {
    position: absolute;
    color: var(--gold);
    font-weight: 500;
    line-height: 1;
    white-space: nowrap;
    letter-spacing: 0.5px;
  }
  .brand-tagline {
    position: absolute;
    color: var(--gold);
    font-weight: 400;
    line-height: 1;
    white-space: nowrap;
    letter-spacing: 0.5px;
  }
  .pen-hand {
    position: absolute;
    background: linear-gradient(160deg, rgba(244,227,28,0.35), rgba(244,227,28,0.12));
    border-radius: 6px;
  }

  .front .brand-name { left: 82px; top: 122px; font-size: 56px; }
  .front .brand-tagline { left: 190px; top: 204px; font-size: 25px; }
  .front .pen-hand { left: 458px; top: 196px; width: 140px; height: 92px; }

  .contact { position: absolute; left: 445px; top: 298px; color: var(--white); }
  .contact__name { font-size: 29px; font-weight: 500; line-height: 1; margin-bottom: 12px; }
  .contact__row { display: flex; align-items: center; gap: 12px; font-size: 22px; line-height: 1; margin-bottom: 13px; }
  .contact__row svg { width: 20px; height: 20px; flex: none; }
  .contact__row svg * { fill: none; stroke: var(--white); stroke-width: 1.6; stroke-linejoin: round; stroke-linecap: round; }

  .back .brand-name { left: 60px; top: 66px; font-size: 46px; }
  .back .brand-tagline { left: 144px; top: 134px; font-size: 20px; }
  .back .pen-hand { left: 360px; top: 132px; width: 118px; height: 72px; }

  .quote { position: absolute; left: 40px; top: 226px; width: 300px; height: 170px; color: var(--white); }
  .quote__mark {
    position: absolute;
    left: 0; top: 0;
    font-family: "Great Vibes", cursive;
    font-size: 110px;
    line-height: 1;
    height: 40px;
    overflow: visible;
  }
  .quote__text {
    position: absolute;
    left: 20px; top: 34px;
    font-family: "Great Vibes", cursive;
    font-size: 42px;
    line-height: 50px;
    width: 290px;
  }

  .divider { position: absolute; left: 349px; top: 216px; width: 1px; height: 226px; background: var(--rule); }

  .occasions { position: absolute; left: 383px; top: 266px; list-style: none; color: var(--white); }
  .occasions li { display: flex; align-items: center; gap: 12px; font-size: 22px; height: 29.6px; white-space: nowrap; }
  .occasions .bullet { width: 7px; height: 7px; border: 1px solid var(--icon); border-radius: 50%; flex: none; }
</style>
</head>
<body>

<section class="card card--front front">
  <div class="flourish" role="img" aria-label="Faint decorative calligraphic flourish in the background"></div>
  <div class="brand-name">Lines for Always</div>
  <div class="brand-tagline">Personalised Poetry</div>
  <div class="pen-hand" role="img" aria-label="Line illustration of a hand writing with a fountain pen"></div>
  <div class="contact">
    <p class="contact__name">Owen Marlowe</p>
    <p class="contact__row">
      <svg viewBox="0 0 20 20" aria-hidden="true"><path d="M4 3 L7 3 L8.5 7 L6.5 8.5 C7.5 10.8 9.2 12.5 11.5 13.5 L13 11.5 L17 13 L17 16 C17 17 16 17.5 15 17.5 C8.5 17 3 11.5 2.5 5 C2.5 4 3 3 4 3 Z"/><path d="M12 3.5 C14.5 4 16 5.5 16.5 8"/><path d="M12 6 C13.2 6.3 14 7.1 14.2 8.2"/></svg>
      <span>0400.552.173</span>
    </p>
    <p class="contact__row">
      <svg viewBox="0 0 20 20" aria-hidden="true"><rect x="2" y="4.5" width="16" height="11" rx="1"/><path d="M2.5 5 L10 11 L17.5 5"/></svg>
      <span>owen@linesforalways.com</span>
    </p>
  </div>
</section>

<section class="card card--back back">
  <div class="flourish" role="img" aria-label="Faint decorative calligraphic flourish in the background"></div>
  <div class="brand-name">Lines for Always</div>
  <div class="brand-tagline">Personalised Poetry</div>
  <div class="pen-hand" role="img" aria-label="Line illustration of a hand writing with a fountain pen"></div>

  <blockquote class="quote">
    <span class="quote__mark">&ldquo;</span>
    <p class="quote__text">Momentous Life Events Personalised in Poetry</p>
  </blockquote>

  <div class="divider"></div>

  <ul class="occasions">
    <li><span class="bullet"></span>Weddings &amp; Anniversaries</li>
    <li><span class="bullet"></span>Birthdays &amp; Christmas</li>
    <li><span class="bullet"></span>Valentines Day</li>
    <li><span class="bullet"></span>Retirements, Bussines &amp; Corporate Events</li>
    <li><span class="bullet"></span>Funerals &amp; Eulogies</li>
  </ul>
</section>

</body>
</html>
```